Broschüre Personalberatung
Zielgruppe
Personalberatung im technischen Umfeld für Führungskräfte und spezialisierte Experten
Aufgabenstellung
Es soll eine neue Firmenpräsentation für PDF Versand designt werden. Nur das Design der Seiten mit Kästen für Texte. Es sollen die Rauten / eckigen Kanten die um das Logo herum sind sich wieder in dem Layout wiederfinden. Die Deckseite von der angehängten Firmenpräsentation finde ich z.B. nicht schlecht. Keine Runden Elemente, gerne klare Linien wie in den Beispielen unten. Das Layout muss zum Schluss in Canva bereitgestellt werden, damit wir es auch weiter bearbeiten können. Die Farben sollen sich aus dem logo und dem generellen Auftritt wieder finden können. Stil soll seriös und professionell sein

```html
<!DOCTYPE html>
<html lang="de">
<head>
<meta charset="utf-8">
<title>VARNO executive – Firmenpräsentation</title>
<link href="https://fonts.googleapis.com/css2?family=Oswald:wght@400;500;600;700&family=Lato:wght@400;700&display=swap" rel="stylesheet">
<style>
  :root{
    --navy:#0c1a33;
    --navy-deep:#081327;
    --blue:#2a9ad6;
    --blue-soft:#5fb4e3;
    --white:#ffffff;
    --ink:#1c2740;
    --grey:#5a6478;
    --stage:#ebebe8;
    --panel:#e6edf4;
  }
  *{box-sizing:border-box;margin:0;padding:0}
  html,body{width:1200px;height:1200px;overflow:hidden}
  body{background:var(--stage);font-family:"Lato",Arial,sans-serif;color:var(--ink);position:relative}
  .page{position:absolute;width:340px;height:482px;overflow:hidden;background:var(--white)}
  .page--cover{left:207px;top:100px}
  .page--intro{left:661px;top:100px;background:var(--navy)}
  .page--profile{left:200px;top:594px}
  .page--competence{left:668px;top:592px}
  .page-art{position:absolute;inset:0;width:100%;height:100%}
  .abs{position:absolute}
  .display{font-family:"Oswald",Arial,sans-serif;font-weight:600;text-transform:uppercase;line-height:1.2}
  .body-copy{font-size:6.3px;line-height:1.5}
  .page-tag{position:absolute;left:22px;top:14px;display:flex;align-items:center;gap:6px;font-size:6px}
  .page-tag svg{width:14px;height:12px}
  .rule{position:absolute;height:1.5px;width:34px;background:var(--blue)}

  /* cover */
  .brand{left:18px;top:58px;width:110px;display:flex;flex-direction:column;align-items:center;gap:6px}
  .brand-mark{width:10px;height:10px;background:var(--blue)}
  .brand-name{font-family:"Oswald",Arial,sans-serif;font-weight:500;font-size:15px;line-height:1.15;color:var(--navy);letter-spacing:1.5px;text-align:center}
  .cover-services{left:205px;top:16px;font-family:"Oswald",Arial,sans-serif;font-size:7px;letter-spacing:1.1px;color:var(--white);line-height:1.5}
  .cover-lead{left:18px;top:152px;font-size:6.4px;color:var(--grey);width:130px;line-height:1.45}
  .cover-title{left:18px;top:198px;font-size:20px;color:var(--navy)}
  .cover-sub{left:18px;top:321px;font-size:6.4px;color:var(--grey);width:120px;line-height:1.5}
  .cover-web{left:18px;top:432px;display:flex;align-items:center;gap:6px;font-size:6px;color:var(--grey)}

  /* intro */
  .intro-title{left:22px;top:44px;font-size:29px;color:var(--white)}
  .intro-copy{left:22px;top:228px;width:200px;color:#d5dceb}
  .intro-copy p+p{margin-top:7px}
  .values{position:absolute;left:14px;top:362px;width:312px;display:flex}
  .value{flex:1;text-align:center;padding:0 6px;border-left:1px solid var(--blue)}
  .value:first-child{border-left:none}
  .value svg{width:40px;height:34px;display:block;margin:0 auto 8px}
  .value-label{font-family:"Oswald",Arial,sans-serif;font-size:6.6px;letter-spacing:.6px;color:var(--blue);margin-bottom:5px}
  .value-text{font-size:6px;line-height:1.5;color:#d5dceb}

  /* profile */
  .profile-title{left:28px;top:46px;font-size:19px;color:var(--navy)}
  .profile-title span{color:var(--blue)}
  .profile-quote{left:28px;top:340px;width:140px;color:var(--white);font-size:9px;line-height:1.5}
  .quote-mark{font-family:"Oswald",Arial,sans-serif;font-size:22px;color:var(--blue);line-height:1;display:block;margin-bottom:6px}
  .person-name{left:198px;top:46px;font-size:19px;color:var(--navy)}
  .person-role{left:198px;top:97px;font-family:"Oswald",Arial,sans-serif;font-size:7px;letter-spacing:.8px;color:var(--blue)}
  .person-copy{left:198px;top:118px;width:118px;color:var(--grey)}
  .person-copy p+p{margin-top:5px}
  .facts{position:absolute;left:198px;top:202px;width:120px}
  .fact{display:flex;gap:7px;align-items:flex-start;height:51px;border-bottom:1px solid var(--blue);padding-top:6px}
  .fact svg{flex:none;width:30px;height:27px}
  .fact-head{font-family:"Oswald",Arial,sans-serif;font-size:5.6px;font-weight:600;color:var(--navy);margin-bottom:2px}
  .fact-text{font-size:5px;line-height:1.4;color:var(--grey)}

  /* competence */
  .comp-title{left:28px;top:32px;font-size:19px;color:var(--navy)}
  .comp-title span{color:var(--blue)}
  .comp-copy{left:28px;top:96px;width:130px;color:var(--grey)}
  .approach{left:28px;top:160px;font-family:"Oswald",Arial,sans-serif;font-size:7px;font-weight:500;color:var(--navy)}
  .approach span{color:var(--blue)}
  .timeline{position:absolute;left:28px;top:180px;width:150px;border-left:1.5px solid var(--navy)}
  .step{position:relative;padding:0 0 8px 18px;height:30px}
  .step::before{content:"";position:absolute;left:-6px;top:2px;width:10px;height:10px;background:var(--navy);clip-path:polygon(25% 0,75% 0,100% 50%,75% 100%,25% 100%,0 50%)}
  .step-head{font-family:"Oswald",Arial,sans-serif;font-size:5.6px;font-weight:600;color:var(--navy)}
  .step-text{font-size:4.8px;line-height:1.4;color:var(--grey)}
  .sectors{position:absolute;left:28px;top:406px;width:300px;height:56px;background:var(--panel);display:flex;align-items:center;padding:0 10px;gap:8px}
  .sectors-hex{width:42px;height:37px;flex:none}
  .sectors-head{font-family:"Oswald",Arial,sans-serif;font-size:5.6px;font-weight:600;color:var(--navy);position:absolute;left:64px;top:6px}
  .sectors-head span{color:var(--blue)}
  .sector{display:flex;gap:4px;align-items:flex-start;margin-top:12px;padding-left:6px;border-left:1px solid #b9c6d6}
  .sector:first-of-type{border-left:none;padding-left:0}
  .sector svg{width:12px;height:12px;flex:none}
  .sector-name{font-family:"Oswald",Arial,sans-serif;font-size:5.4px;color:var(--blue)}
  .sector-text{font-size:4.6px;line-height:1.3;color:var(--grey)}
</style>
</head>
<body>

<!-- Cover -->
<section class="page page--cover">
  <svg class="page-art" viewBox="0 0 340 482" preserveAspectRatio="none">
    <defs>
      <linearGradient id="plantNight" x1="0" y1="0" x2="0" y2="1">
        <stop offset="0" stop-color="#0a1730"/>
        <stop offset=".55" stop-color="#15284a"/>
        <stop offset="1" stop-color="#0b1426"/>
      </linearGradient>
    </defs>
    <rect x="120" y="0" width="220" height="482" fill="url(#plantNight)" role="img" aria-label="Nachtaufnahme einer beleuchteten Industrieanlage"/>
    <polygon points="0,0 122,0 228,236 122,482 0,482" fill="var(--white)"/>
    <polyline points="128,0 234,236 128,482" fill="none" stroke="var(--blue)" stroke-width="1.2"/>
    <polygon points="0,0 14,0 0,58" fill="var(--navy)"/>
    <polygon points="0,34 14,0 14,32 0,62" fill="var(--blue)"/>
    <polygon points="163,330 206,355 206,405 163,430 120,405 120,355" fill="var(--white)" stroke="var(--blue)" stroke-width="3"/>
    <polygon points="163,337 200,358 200,402 163,423 126,402 126,358" fill="#3f5878" role="img" aria-label="Foto: Handschlag zweier Geschäftsleute"/>
  </svg>
  <div class="abs brand"><span class="brand-mark"></span><span class="brand-name">VARNO<br>executive</span></div>
  <div class="abs cover-services">EXECUTIVE SEARCH<br>TALENT ACQUISITION<br>LEADERSHIP SOLUTIONS</div>
  <p class="abs cover-lead">Ihre spezialisierte Personalberatung im technischen Umfeld</p>
  <span class="rule" style="left:18px;top:186px"></span>
  <h1 class="abs display cover-title">Wir finden<br>die besten<br>Köpfe.</h1>
  <span class="rule" style="left:18px;top:310px;background:#c9d2de"></span>
  <p class="abs cover-sub">Für die TGA-, Elektro- und Maschinenbau-Branche</p>
  <div class="abs cover-web">
    <svg width="12" height="11" viewBox="0 0 12 11"><polygon points="3,0 9,0 12,5.5 9,11 3,11 0,5.5" fill="var(--navy)"/></svg>
    www.varno-exec.de
  </div>
</section>

<!-- Intro -->
<section class="page page--intro">
  <svg class="page-art" viewBox="0 0 340 482" preserveAspectRatio="none">
    <defs>
      <linearGradient id="plantGlow" x1="0" y1="0" x2="1" y2="1">
        <stop offset="0" stop-color="#1b2f52"/>
        <stop offset=".6" stop-color="#2a4268"/>
        <stop offset="1" stop-color="#0e1c36"/>
      </linearGradient>
    </defs>
    <polygon points="175,0 340,0 340,385 175,385 290,192" fill="url(#plantGlow)" role="img" aria-label="Beleuchtete Raffinerie bei Nacht"/>
    <polyline points="175,0 290,192 175,385" fill="none" stroke="var(--blue)" stroke-width="1.2"/>
  </svg>
  <div class="page-tag" style="color:#c7d0df">
    <svg viewBox="0 0 14 12"><polygon points="3.5,0 10.5,0 14,6 10.5,12 3.5,12 0,6" fill="var(--blue)"/></svg>Page 2
  </div>
  <h2 class="abs display intro-title">Wir<br>finden die<br>besten<br>Köpfe.</h2>
  <span class="rule" style="left:22px;top:212px"></span>
  <div class="abs body-copy intro-copy">
    <p>VARNO executive ist Ihr bevorzugter Partner, wenn es um die Besetzung technisch anspruchsvoller Fach- und Führungspositionen geht.</p>
    <p>Mit fundiertem Branchenverständnis und einem strukturierten Suchprozess identifizieren wir gezielt die richtigen Persönlichkeiten für nachhaltigen Unternehmenserfolg.</p>
  </div>
  <div class="values">
    <div class="value">
      <svg viewBox="0 0 40 34"><polygon points="10,1 30,1 39,17 30,33 10,33 1,17" fill="none" stroke="var(--blue)" stroke-width="1.3"/></svg>
      <div class="value-label">SPEZIALISIERT</div>
      <div class="value-text">Fokus auf TGA, Elektrotechnik und Maschinenbau.</div>
    </div>
    <div class="value">
      <svg viewBox="0 0 40 34"><polygon points="10,1 30,1 39,17 30,33 10,33 1,17" fill="none" stroke="var(--blue)" stroke-width="1.3"/></svg>
      <div class="value-label">PRÄZISE</div>
      <div class="value-text">Zielgerichtete Suche mit tiefem Branchenverständnis und technischem Know-how.</div>
    </div>
    <div class="value">
      <svg viewBox="0 0 40 34"><polygon points="10,1 30,1 39,17 30,33 10,33 1,17" fill="none" stroke="var(--blue)" stroke-width="1.3"/></svg>
      <div class="value-label">VERLÄSSLICH</div>
      <div class="value-text">Vertraulich, partnerschaftlich und mit klarer Verantwortung für Ihren Erfolg.</div>
    </div>
  </div>
</section>

<!-- Profile -->
<section class="page page--profile">
  <svg class="page-art" viewBox="0 0 340 482" preserveAspectRatio="none">
    <rect x="0" y="0" width="14" height="482" fill="var(--navy)"/>
    <polygon points="0,300 168,300 196,482 0,482" fill="var(--navy)"/>
    <polyline points="168,300 196,482" fill="none" stroke="var(--blue)" stroke-width="1.2"/>
    <line x1="328" y1="20" x2="328" y2="470" stroke="var(--blue)" stroke-width="1"/>
    <polygon points="97,142 177,188 177,280 97,326 17,280 17,188" fill="var(--white)" stroke="var(--blue)" stroke-width="2.5"/>
    <polygon points="97,150 170,192 170,276 97,318 24,276 24,192" fill="#7d8ea3" role="img" aria-label="Porträtfoto des Geschäftsführers am Laptop"/>
  </svg>
  <div class="page-tag" style="color:var(--grey)">
    <svg viewBox="0 0 14 12"><polygon points="3.5,0 10.5,0 14,6 10.5,12 3.5,12 0,6" fill="var(--blue)"/></svg>Page 3
  </div>
  <h2 class="abs display profile-title">Persönlich.<br><span>Kompetent.</span><br><span>Verbunden.</span></h2>
  <blockquote class="abs profile-quote"><span class="quote-mark">&#8220;</span>Mein Anspruch ist es, nicht nur passende Profile zu finden, sondern echte Mehrwerte für Unternehmen und Talente zu schaffen.&#8220;</blockquote>
  <h3 class="abs display person-name">Kerem<br>Aldoğan</h3>
  <div class="abs person-role">GESCHÄFTSFÜHRER</div>
  <div class="abs body-copy person-copy">
    <p>Als Geschäftsführer stehe ich persönlich dafür, dass jede Suche mit höchster Sorgfalt, Diskretion und technischem Verständnis durchgeführt wird.</p>
    <p>Unser Anspruch ist es, nicht nur passende Profile zu finden, sondern nachhaltige Mehrwerte für Unternehmen und Talente zu schaffen.</p>
  </div>
  <div class="facts">
    <div class="fact"><svg viewBox="0 0 30 27"><polygon points="7.5,1 22.5,1 29,13.5 22.5,26 7.5,26 1,13.5" fill="var(--navy)" stroke="var(--blue)" stroke-width="1"/></svg><div><div class="fact-head">MEHR ALS 10 JAHRE ERFAHRUNG</div><div class="fact-text">in Executive Search und Personalberatung für technische Branchen.</div></div></div>
    <div class="fact"><svg viewBox="0 0 30 27"><polygon points="7.5,1 22.5,1 29,13.5 22.5,26 7.5,26 1,13.5" fill="var(--navy)" stroke="var(--blue)" stroke-width="1"/></svg><div><div class="fact-head">TIEFES BRANCHENVERSTÄNDNIS</div><div class="fact-text">in TGA, Elektrotechnik und Maschinenbau im DACH-Raum.</div></div></div>
    <div class="fact"><svg viewBox="0 0 30 27"><polygon points="7.5,1 22.5,1 29,13.5 22.5,26 7.5,26 1,13.5" fill="var(--navy)" stroke="var(--blue)" stroke-width="1"/></svg><div><div class="fact-head">VERLÄSSLICHER PARTNER</div><div class="fact-text">für mittelständische Unternehmen und internationale Konzerne.</div></div></div>
    <div class="fact"><svg viewBox="0 0 30 27"><polygon points="7.5,1 22.5,1 29,13.5 22.5,26 7.5,26 1,13.5" fill="var(--navy)" stroke="var(--blue)" stroke-width="1"/></svg><div><div class="fact-head">DISKRETION &amp; INTEGRITÄT</div><div class="fact-text">als Grundlage jeder erfolgreichen Zusammenarbeit.</div></div></div>
    <div class="fact"><svg viewBox="0 0 30 27"><polygon points="7.5,1 22.5,1 29,13.5 22.5,26 7.5,26 1,13.5" fill="var(--navy)" stroke="var(--blue)" stroke-width="1"/></svg><div><div class="fact-head">KLARE ERGEBNISORIENTIERUNG</div><div class="fact-text">mit Fokus auf nachhaltige und passgenaue Besetzungen.</div></div></div>
  </div>
</section>

<!-- Competence -->
<section class="page page--competence">
  <svg class="page-art" viewBox="0 0 340 482" preserveAspectRatio="none">
    <defs>
      <linearGradient id="towerBlue" x1="0" y1="0" x2="0" y2="1">
        <stop offset="0" stop-color="#8aa9c9"/>
        <stop offset=".45" stop-color="#2f5486"/>
        <stop offset="1" stop-color="#0f2446"/>
      </linearGradient>
    </defs>
    <polygon points="205,0 340,0 340,482 110,482 275,80" fill="url(#towerBlue)" role="img" aria-label="Moderne Glasfassade eines Bürogebäudes in Blautönen"/>
    <polyline points="205,0 275,80 110,482" fill="none" stroke="var(--blue)" stroke-width="1.2"/>
    <rect x="0" y="0" width="8" height="482" fill="var(--navy)"/>
    <polygon points="0,466 340,470 340,482 0,482" fill="var(--navy)"/>
  </svg>
  <div class="page-tag" style="color:var(--grey)">
    <svg viewBox="0 0 14 12"><polygon points="3.5,0 10.5,0 14,6 10.5,12 3.5,12 0,6" fill="var(--blue)"/></svg>Page 4
  </div>
  <h2 class="abs display comp-title">Unsere Kompetenz.<br><span>Ihr Vorsprung.</span></h2>
  <p class="abs body-copy comp-copy">VARNO executive steht für die präzise Besetzung technischer Schlüsselpositionen. Wir verbinden tiefes Branchenwissen mit einem strukturierten und effizienten Suchprozess – für messbare Ergebnisse und nachhaltigen Erfolg.</p>
  <div class="abs approach">UNSER ANSATZ – <span>IHR VORTEIL</span></div>
  <div class="timeline">
    <div class="step"><div class="step-head">ZIELGERICHTET</div><div class="step-text">Wir verstehen Ihre Anforderungen und identifizieren gezielt die passenden Führungspersönlichkeiten.</div></div>
    <div class="step"><div class="step-head">PERSÖNLICH</div><div class="step-text">Direkter Kontakt, individuelle Beratung und enge Begleitung in jedem Schritt.</div></div>
    <div class="step"><div class="step-head">DISKRET</div><div class="step-text">Vertraulichkeit und Professionalität sind für uns selbstverständlich.</div></div>
    <div class="step"><div class="step-head">EFFIZIENT</div><div class="step-text">Strukturierte Prozesse und ein starkes Netzwerk sparen Zeit und sichern Qualität.</div></div>
    <div class="step"><div class="step-head">NACHHALTIG</div><div class="step-text">Langfristige Besetzungen für stabile Teams und nachhaltigen Unternehmenserfolg.</div></div>
  </div>
  <div class="sectors">
    <svg class="sectors-hex" viewBox="0 0 42 37"><polygon points="10.5,1 31.5,1 41,18.5 31.5,36 10.5,36 1,18.5" fill="var(--navy)" stroke="var(--blue)" stroke-width="1"/></svg>
    <div class="sectors-head">UNSERE BRANCHENEXPERTISE<br><span>FÜR IHREN ERFOLG</span></div>
    <div class="sector">
      <svg viewBox="0 0 12 12"><path d="M1 11V5l5-4 5 4v6H1z" fill="none" stroke="var(--navy)" stroke-width="1"/></svg>
      <div><div class="sector-name">TGA</div><div class="sector-text">Technische Gebäudeausrüstung</div></div>
    </div>
    <div class="sector">
      <svg viewBox="0 0 12 12"><path d="M7 1L2 7h4l-1 4 5-6H6l1-4z" fill="none" stroke="var(--navy)" stroke-width="1"/></svg>
      <div><div class="sector-name">ELEKTROTECHNIK</div><div class="sector-text">Energie- und Elektrotechnik</div></div>
    </div>
    <div class="sector">
      <svg viewBox="0 0 12 12"><polygon points="4,1 8,1 11,6 8,11 4,11 1,6" fill="none" stroke="var(--navy)" stroke-width="1"/><rect x="5" y="5" width="2" height="2" fill="var(--navy)"/></svg>
      <div><div class="sector-name">MASCHINENBAU</div><div class="sector-text">Maschinen- und Anlagenbau</div></div>
    </div>
  </div>
</section>

</body>
</html>
```